Redesign of my Homepage - Online resource for anyone to learn American Sign Language

I would like to have a new homepage design http://www.SignPathora.com . My business is a website for anyone to learn American Sign Language. There are over 300 video lessons, with each lesson having 20 vocabulary words, retention exercises, 16,000 video dictionary etc. It is a very extensive site. It is a self paced website. If you need a log in to see what customers see, please let me know. I would like to keep the same color scheme. I want the website to look modern and clean. I want a fresh look! I want something that is easy to navigate, attracts customers, and easy to follow. I would like the final design to communicate that my website is for anyone to learn how to sign with this incredible program.

Target Market(s)

Students taking American Sign Language, Parents with Deaf children, future interpreters for the deaf, co-workers of the Deaf. Also, schools that offer American Sign Language (online schools, homeschools, etc. ).

Industry/Entity Type

Business

Number of Pages Required

1 page

Requirements
Must have
• My project must be very clean and clear. I want my homepage to show that this is a program for people to learn how American Sign Language.
Nice to have
• Not sure. Surprise me.

```html
<!DOCTYPE html>
<html lang="en">
<head>
<meta charset="utf-8">
<title>SignPathora – Learn American Sign Language</title>
<link href="https://fonts.googleapis.com/css2?family=Ubuntu:wght@400;500&display=swap" rel="stylesheet">
<style>
  :root{
    --green:#2fb457;
    --green-dark:#0b5f12;
    --nav-active:#0b5f12;
    --ink:#111;
    --text:#555;
    --bg-soft:#eeeeee;
    --bg-bar:#d9d9d9;
    --purple:#5b1f99;
    --blue:#203f9f;
    --red:#c1161c;
    --white:#fff;
  }
  *{box-sizing:border-box;margin:0;padding:0}
  html,body{width:837px;height:1200px;overflow:hidden}
  body{font-family:"Ubuntu",sans-serif;background:var(--bg-soft);color:var(--text);position:relative}
  a{text-decoration:none;color:inherit}

  .site-header{position:absolute;top:0;left:0;width:837px;height:98px;background:var(--white)}
  .brand{position:absolute;left:33px;top:30px;display:flex;align-items:center;gap:8px;font-size:30px;font-weight:500;color:var(--green)}
  .brand-dot{width:14px;height:14px;border-radius:50%;background:var(--green)}
  .account{position:absolute;right:33px;top:16px;display:flex;align-items:center;gap:18px;font-size:13px}
  .account .sign-in{color:#777}
  .account .sign-up{background:var(--green);color:var(--white);padding:9px 12px;border-radius:3px}

  .main-nav{position:absolute;top:98px;left:0;width:837px;height:33px;background:var(--green);display:flex;align-items:center;padding-left:34px;gap:20px;font-size:12px;color:var(--white)}
  .main-nav a{position:relative;line-height:33px;display:flex;align-items:center;gap:4px}
  .main-nav .active{color:var(--nav-active)}
  .main-nav .active::after{content:"";position:absolute;left:0;right:0;bottom:6px;height:3px;background:var(--nav-active)}
  .chev{width:8px;height:6px}

  .hero{position:absolute;top:131px;left:0;width:837px;height:361px;overflow:hidden}
  .hero-photo{position:absolute;inset:0;background:linear-gradient(100deg,#c9a58c 0%,#e8d4c9 35%,#b8a69a 60%,#d7d0c8 100%)}
  .hero-shape{position:absolute;inset:0}
  .hero-copy{position:absolute;left:540px;top:125px;width:200px;text-align:center}
  .hero-copy .big{font-size:60px;font-weight:500;color:var(--ink);line-height:56px}
  .hero-copy .sub{font-size:34px;color:var(--white);margin-top:6px}
  .hero-copy .cta{display:inline-block;margin-top:14px;background:var(--green-dark);color:var(--white);font-size:18px;width:163px;height:39px;line-height:39px;border-radius:3px}
  .arrow{position:absolute;top:160px;width:24px;height:42px}
  .arrow.prev{left:32px}
  .arrow.next{right:34px}
  .dots{position:absolute;left:393px;top:329px;display:flex;gap:5px}
  .dots span{width:9px;height:9px;border-radius:50%;background:var(--green)}
  .dots span.on{background:var(--green-dark)}

  .audiences{position:absolute;top:558px;left:33px;display:flex;gap:16px}
  .card{width:246px;height:361px;background:var(--white);position:relative;box-shadow:0 1px 3px rgba(0,0,0,.12)}
  .card-photo{height:181px}
  .card-bar{height:8px}
  .card h2{font-size:21px;font-weight:500;line-height:28px;margin:14px 16px 8px 16px}
  .card p{font-size:13px;line-height:19px;margin:0 16px;color:var(--text)}
  .learn-more{position:absolute;right:16px;bottom:18px;display:flex;align-items:center;gap:8px;font-size:14px;color:var(--text)}
  .learn-more svg{width:11px;height:20px}
  .card.community h2{color:var(--purple)} .card.community .card-bar{background:var(--purple)}
  .card.parents h2{color:var(--blue)} .card.parents .card-bar{background:var(--blue)}
  .card.students h2{color:var(--red)} .card.students .card-bar{background:var(--red)}
  .card.community .card-photo{background:linear-gradient(180deg,#bfb8b0,#8d7f74)}
  .card.parents .card-photo{background:linear-gradient(180deg,#d6b189,#9f8a83)}
  .card.students .card-photo{background:linear-gradient(90deg,#d98aa7,#d9d3cc 50%,#4d6ec8)}

  .site-footer{position:absolute;top:985px;left:0;width:837px;height:215px;border-top:1px solid #ddd;background:var(--bg-soft)}
  .footer-brand{position:absolute;top:42px;left:0;width:837px;text-align:center;font-size:28px;font-weight:500;color:var(--green)}
  .footer-links{position:absolute;top:116px;left:0;width:837px;text-align:center;font-size:12px;color:#444}
  .footer-links span{margin:0 7px}
  .legal{position:absolute;bottom:0;left:0;width:837px;height:51px;line-height:51px;background:var(--bg-bar);text-align:center;font-size:12px;color:#222}
</style>
</head>
<body>
  <header class="site-header">
    <a class="brand" href="#"><span class="brand-dot"></span>SignPathora</a>
    <div class="account">
      <a class="sign-in" href="#">Sign In</a>
      <a class="sign-up" href="#">Sign Up</a>
    </div>
  </header>

  <nav class="main-nav">
    <a class="active" href="#">Home</a>
    <a href="#">How it works <svg class="chev" viewBox="0 0 8 6"><path d="M1 1l3 3 3-3" stroke="#fff" stroke-width="1.6" fill="none"/></svg></a>
    <a href="#">Gift Certificates</a>
    <a href="#">Try it Free</a>
    <a href="#">Buy Now</a>
    <a href="#">Contact Us <svg class="chev" viewBox="0 0 8 6"><path d="M1 1l3 3 3-3" stroke="#fff" stroke-width="1.6" fill="none"/></svg></a>
    <a href="#">Group Rate Form</a>
    <a href="#">Teacher's Guide</a>
  </nav>

  <section class="hero">
    <div class="hero-photo" role="img" aria-label="Young girl and her teacher pointing at a computer screen while learning sign language"></div>
    <svg class="hero-shape" viewBox="0 0 837 361" preserveAspectRatio="none">
      <path d="M650 0 C560 60 480 220 500 361 L837 361 L837 0 Z" fill="#2fb457"/>
    </svg>
    <svg class="arrow prev" viewBox="0 0 24 42"><path d="M20 3L4 21l16 18" stroke="#fff" stroke-width="3" fill="none"/></svg>
    <svg class="arrow next" viewBox="0 0 24 42"><path d="M4 3l16 18L4 39" stroke="#fff" stroke-width="3" fill="none"/></svg>
    <div class="hero-copy">
      <div class="big">ASL</div>
      <div class="sub">Tutor Online</div>
      <a class="cta" href="#">Sign Up Today</a>
    </div>
    <div class="dots"><span></span><span class="on"></span><span></span><span></span></div>
  </section>

  <main class="audiences">
    <article class="card community">
      <div class="card-photo" role="img" aria-label="Group of adults signing together in a class"></div>
      <div class="card-bar"></div>
      <h2>Learning Community</h2>
      <p>Anyone that has a passion to learn American Sign Language (ASL)</p>
      <a class="learn-more" href="#">Learn more <svg viewBox="0 0 11 20"><path d="M2 2l7 8-7 8" stroke="#5b1f99" stroke-width="2.6" fill="none"/></svg></a>
    </article>
    <article class="card parents">
      <div class="card-photo" role="img" aria-label="Mother signing with her young child"></div>
      <div class="card-bar"></div>
      <h2>Hearing Parents of Deaf Children</h2>
      <p>Learn to communicate more effectively with your child</p>
      <a class="learn-more" href="#">Learn more <svg viewBox="0 0 11 20"><path d="M2 2l7 8-7 8" stroke="#203f9f" stroke-width="2.6" fill="none"/></svg></a>
    </article>
    <article class="card students">
      <div class="card-photo" role="img" aria-label="Student and tutor signing in front of a laptop"></div>
      <div class="card-bar"></div>
      <h2>Deaf and Hard of Hearing Students</h2>
      <p>Learn to tackle the challenges you faced in the classroom</p>
      <a class="learn-more" href="#">Learn more <svg viewBox="0 0 11 20"><path d="M2 2l7 8-7 8" stroke="#c1161c" stroke-width="2.6" fill="none"/></svg></a>
    </article>
  </main>

  <footer class="site-footer">
    <div class="footer-brand">SignPathora</div>
    <div class="footer-links"><a href="#">Contact Us</a><span>|</span><a href="#">Our Mission</a><span>|</span><a href="#">Terms &amp; Conditions</a></div>
    <div class="legal">SignPathora ©2017 All Rights Reserved | 1485425070.9769s</div>
  </footer>
</body>
</html>
```